Brightmere Business Card Redesign & Logo Update

We need to update our business cards to something more modern and fresh. Brightmere can provide the current color schemes and old design examples, but welcome creativity in helping us with this redesign. PLEASE NOTE that we no longer utilize the "tree" and/or "leaf" imagery in our branding. If able would apprecaite an update on the quality of our "words only" logo in Ai. / PNG formats too.

Target Market(s)

Investors, landowners, corporate partners, contractors

Industry/Entity Type

Environmental Restoration & Conservation

Contact Information for Business Card

Logo, persons name, title, mailing address, phone and email, website url

Font styles to use
Other font styles liked:
• Merriweather

Requirements
Nice to have
• Logo, persons name, title, mailing address, phone and email, website url, but open to ideams
Should not have
• No all back backgrounds

```html
<!DOCTYPE html>
<html lang="en">
<head>
<meta charset="utf-8">
<title>Brightmere Business Card</title>
<link rel="stylesheet" href="https://fonts.googleapis.com/css2?family=Source+Sans+3:wght@400;700&display=swap">
<style>
  :root {
    --green: #13753d;
    --orange: #e67a22;
    --paper: #f4f4f4;
    --backdrop: #e4e4e4;
    --white: #ffffff;
  }
  * { margin: 0; padding: 0; box-sizing: border-box; }
  html, body {
    width: 1200px; height: 960px; overflow: hidden;
    background: var(--backdrop);
    font-family: "Source Sans 3", sans-serif;
  }
  .card {
    position: absolute; left: 296px; width: 612px; height: 350px;
    border-radius: 22px; overflow: hidden;
  }
  .card-front { top: 105px; display: flex; }
  .front-half { height: 100%; }
  .front-half--green { width: 301px; background: var(--green); }
  .front-half--orange { flex: 1; background: var(--orange); }
  .front-wordmark {
    position: absolute; left: 0; right: 0; top: 138px;
    text-align: center; color: var(--white);
    font-weight: 700; font-size: 54px; letter-spacing: 2px; line-height: 1;
    text-transform: uppercase;
  }

  .card-back { top: 508px; background: var(--paper); }
  .back-shapes { position: absolute; inset: 0; }
  .back-wordmark {
    position: absolute; left: 36px; top: 140px; width: 290px;
    text-align: center; color: var(--green);
    font-weight: 700; font-size: 40px; letter-spacing: 1px; line-height: 1;
    text-transform: uppercase;
  }
  .person {
    position: absolute; right: 30px; top: 68px; text-align: right; color: var(--white);
  }
  .person-name { font-weight: 700; font-size: 20px; line-height: 24px; }
  .person-title { font-size: 16px; line-height: 20px; }
  .contact {
    position: absolute; right: 30px; top: 208px; list-style: none;
    color: var(--white); font-size: 16px; text-align: right;
  }
  .contact li { display: flex; justify-content: flex-end; align-items: center; gap: 6px; line-height: 20px; }
  .contact li.contact-gap { margin-top: 5px; }
  .contact li.no-icon { padding-right: 20px; }
  .contact svg { width: 14px; height: 14px; flex: none; stroke: var(--orange); fill: none; stroke-width: 2; }
</style>
</head>
<body>

<section class="card card-front" aria-label="Card front">
  <div class="front-half front-half--green"></div>
  <div class="front-half front-half--orange"></div>
  <p class="front-wordmark">Brightmere</p>
</section>

<section class="card card-back" aria-label="Card back">
  <svg class="back-shapes" width="612" height="350" viewBox="0 0 612 350" aria-hidden="true">
    <path d="M277,0 L612,0 L612,174 L392,174 Q366,174 354,150 Z" fill="var(--orange)"/>
    <path d="M398,178 L612,178 L612,350 L277,350 L372,192 Q380,178 398,178 Z" fill="var(--green)"/>
  </svg>

  <p class="back-wordmark">Brightmere</p>

  <div class="person">
    <p class="person-name">Daniel Carter</p>
    <p class="person-title">Owner</p>
  </div>

  <ul class="contact">
    <li>418 Meadow Lane, Suite 210
      <svg viewBox="0 0 24 24"><path d="M12 22s7-7 7-12a7 7 0 0 0-14 0c0 5 7 12 7 12z"/><circle cx="12" cy="10" r="2.5"/></svg>
    </li>
    <li class="no-icon">Alder Falls, CA 95012</li>
    <li class="contact-gap">555-204-7183
      <svg viewBox="0 0 24 24"><path d="M5 3h4l2 5-3 2a12 12 0 0 0 6 6l2-3 5 2v4a2 2 0 0 1-2 2A18 18 0 0 1 3 5a2 2 0 0 1 2-2z"/></svg>
    </li>
    <li>daniel@brightmere.com
      <svg viewBox="0 0 24 24"><rect x="3" y="5" width="18" height="14" rx="1"/><path d="M3 6l9 7 9-7"/></svg>
    </li>
    <li>www.brightmere.com
      <svg viewBox="0 0 24 24"><circle cx="12" cy="12" r="9"/><path d="M3 12h18M12 3c3 3 3 15 0 18M12 3c-3 3-3 15 0 18"/></svg>
    </li>
  </ul>
</section>

</body>
</html>
```